Design some Business Cards for Tavro

Thanks to everyone for their efforts. I will just be reviewing the first two entries from each contestant, so I'd suggest withdrawing entries which are not your favorites & going with your best two. Many thanks, Derek

I was after a double sided business card for tavro.com.au. Tavro is a billing app and website for tradesman and service providers who move from site to site.

Firstly design for Derek Holm with mobile 0481 555 907 & email demo@tavro.com.au.

Logo is attached, so please work with those colours. I've also included our url if you believe that is worth building in.

I would like the original working files and the business card will need to be produced for 3 different employees when the winner is selected.

Additional TAVRO text files if this helps.

```html
<!DOCTYPE html>
<html lang="en">
<head>
<meta charset="utf-8">
<title>Tavro Business Card</title>
<link rel="stylesheet" href="https://fonts.googleapis.com/css2?family=Open+Sans:ital,wght@0,400;0,600;0,700;1,400&display=swap">
<style>
  :root {
    --stage: #3a3a3a;
    --brand-blue: #1ca3d8;
    --brand-blue-deep: #1795c8;
    --brand-red: #c21f2a;
    --navy: #1d2a4a;
    --white: #ffffff;
  }
  * { box-sizing: border-box; margin: 0; padding: 0; }
  html, body {
    width: 1200px; height: 851px; overflow: hidden;
    background: var(--stage);
    font-family: "Open Sans", Arial, sans-serif;
  }
  .stage {
    position: relative; width: 1200px; height: 851px;
    display: flex; align-items: center; justify-content: center; gap: 40px;
  }
  .card {
    position: relative; width: 540px; height: 309px; overflow: hidden;
  }

  /* Front */
  .card-front { background: var(--brand-blue); }
  .card-front .wordmark {
    position: absolute; right: 42px; top: 178px;
    display: flex; align-items: center; gap: 14px;
  }
  .card-front .wordmark-name {
    font-weight: 600; font-size: 54px; letter-spacing: 3px; color: var(--navy); line-height: 1;
  }
  .card-front .wordmark-dot {
    width: 46px; height: 46px; border-radius: 50%; background: var(--white);
  }
  .card-front .site-url {
    position: absolute; right: 46px; top: 244px;
    font-size: 13px; letter-spacing: 1px; color: var(--brand-red); font-weight: 400;
  }

  /* Back */
  .card-back { background: var(--white); }
  .card-back .wordmark {
    position: absolute; left: 150px; top: 66px;
    display: flex; align-items: center; gap: 16px;
  }
  .card-back .wordmark-name {
    font-weight: 600; font-size: 62px; letter-spacing: 3px; color: var(--brand-blue); line-height: 1;
  }
  .card-back .wordmark-dot {
    width: 52px; height: 52px; border-radius: 50%; background: var(--brand-red);
  }
  .identity {
    position: absolute; left: 0; bottom: 0; width: 270px; height: 126px;
    background: var(--brand-blue); border-top-right-radius: 10px;
    padding: 16px 0 0 70px; color: var(--white);
  }
  .identity .person-name { font-weight: 700; font-size: 17px; }
  .identity .person-title { font-size: 15px; padding-left: 52px; margin-top: 1px; }
  .contact {
    position: absolute; right: 0; bottom: 0; width: 270px; height: 112px;
    background: var(--brand-red); color: var(--white);
    padding: 36px 0 0 62px; font-size: 13px; letter-spacing: 0.5px;
  }
  .contact-row { display: flex; align-items: center; gap: 8px; height: 18px; }
  .contact-row svg { width: 11px; height: 11px; flex: none; }
</style>
</head>
<body>
<main class="stage">
  <section class="card card-front" aria-label="Card front">
    <div class="wordmark">
      <span class="wordmark-dot"></span>
      <span class="wordmark-name">TAVRO</span>
    </div>
    <p class="site-url">WWW.TAVRO.COM.AU</p>
  </section>

  <section class="card card-back" aria-label="Card back">
    <div class="wordmark">
      <span class="wordmark-dot"></span>
      <span class="wordmark-name">TAVRO</span>
    </div>
    <div class="identity">
      <p class="person-name">Derek Holm</p>
      <p class="person-title">Director</p>
    </div>
    <div class="contact">
      <p class="contact-row">
        <svg viewBox="0 0 12 12"><path fill="#fff" d="M2.5 1l2 2-1 1.3c.6 1.4 1.8 2.6 3.2 3.2L8 6.5l2 2-1.3 1.8C4.8 10 2 7.2 1.7 2.3z"/></svg>
        0481 555 907
      </p>
      <p class="contact-row">
        <svg viewBox="0 0 12 12"><rect x="1" y="2.5" width="10" height="7" fill="#fff"/><path d="M1 2.5l5 4 5-4" stroke="#c21f2a" fill="none"/></svg>
        derek@tavro.com.au
      </p>
      <p class="contact-row">
        <svg viewBox="0 0 12 12"><circle cx="6" cy="6" r="5" fill="#fff"/><path d="M1 6h10M6 1c-2 2.5-2 7.5 0 10M6 1c2 2.5 2 7.5 0 10" stroke="#c21f2a" stroke-width=".8" fill="none"/></svg>
        www.tavro.com.au
      </p>
    </div>
  </section>
</main>
</body>
</html>
```